Bref créative
Tamsel Briar Gifts
making every gift "one of a kind!"
Bright & Fun-filled
Marta Fowler
Owner
no address - online only
fowler@tamselbriargifts.example
www.tamselbriargifts.example
I would like my logo on the front in white background.
I would like my logo in black background.

```html
<!DOCTYPE html>
<html lang="en">
<head>
<meta charset="utf-8">
<title>Tamsel Briar Gifts – Business Card</title>
<link rel="stylesheet" href="https://fonts.googleapis.com/css2?family=Crimson+Text:wght@400;700&display=swap">
<style>
  :root {
    --backdrop: #e8e6e3;
    --card: #ffffff;
    --magenta: #b3207a;
    --gold: #c9a13c;
    --brown: #8d6a2c;
    --ink: #3a3a3a;
    --muted: #7a7a7a;
    --rule: #c9c9c9;
  }
  html, body {
    margin: 0;
    padding: 0;
    width: 1200px;
    height: 780px;
    overflow: hidden;
    background: var(--backdrop);
  }
  .card {
    position: absolute;
    left: 75px;
    top: 90px;
    width: 1050px;
    height: 600px;
    background: var(--card);
    border-radius: 36px;
    overflow: hidden;
    box-shadow: 0 10px 30px rgba(0,0,0,0.18);
    font-family: "Crimson Text", Georgia, serif;
  }
  .brand {
    position: absolute;
    left: 0;
    right: 0;
    top: 140px;
    text-align: center;
  }
  .brand-name {
    margin: 0;
    font-family: "Crimson Text", Georgia, serif;
    font-weight: 400;
    font-size: 80px;
    line-height: 1;
    color: var(--brown);
  }
  .owner {
    position: absolute;
    right: 580px;
    top: 345px;
    text-align: right;
  }
  .owner-name {
    margin: 0;
    font-weight: 700;
    font-size: 46px;
    line-height: 1;
    color: var(--magenta);
  }
  .owner-role {
    margin: 6px 0 0;
    font-size: 26px;
    color: var(--muted);
  }
  .divider {
    position: absolute;
    left: 500px;
    top: 305px;
    width: 2px;
    height: 140px;
    background: var(--rule);
  }
  .contact {
    position: absolute;
    left: 525px;
    top: 300px;
    margin: 0;
    padding: 0;
    list-style: none;
  }
  .contact-item {
    display: flex;
    align-items: center;
    gap: 14px;
    height: 48px;
    font-size: 29px;
    color: var(--ink);
  }
  .contact-icon {
    width: 24px;
    height: 24px;
    flex: none;
  }
  .gold-rule {
    position: absolute;
    left: 0;
    right: 0;
    bottom: 76px;
    height: 4px;
    background: var(--gold);
  }
  .base-band {
    position: absolute;
    left: 0;
    right: 0;
    bottom: 0;
    height: 70px;
    background: var(--magenta);
  }
</style>
</head>
<body>
  <main class="card">
    <header class="brand">
      <h1 class="brand-name">Tamsel Briar Gifts</h1>
    </header>

    <section class="owner">
      <p class="owner-name">Marta Fowler</p>
      <p class="owner-role">Owner</p>
    </section>

    <div class="divider"></div>

    <ul class="contact">
      <li class="contact-item">
        <svg class="contact-icon" viewBox="0 0 24 24" aria-hidden="true">
          <circle cx="12" cy="12" r="12" fill="var(--magenta)"/>
          <path d="M8.5 6.5c.6-.4 1.3-.2 1.6.4l.9 1.9c.2.5.1 1-.3 1.3l-.8.6c.5 1.3 1.5 2.4 2.8 3l.6-.8c.3-.4.9-.5 1.3-.3l1.9.9c.6.3.8 1 .4 1.6l-.6.9c-.5.7-1.4 1-2.2.7-3.2-1.1-5.5-3.4-6.6-6.6-.3-.8 0-1.7.7-2.2z" fill="#fff"/>
        </svg>
        <span>555-014-2287</span>
      </li>
      <li class="contact-item">
        <svg class="contact-icon" viewBox="0 0 24 24" aria-hidden="true">
          <circle cx="12" cy="12" r="12" fill="var(--magenta)"/>
          <circle cx="12" cy="12" r="3" fill="none" stroke="#fff" stroke-width="1.8"/>
          <path d="M15 9v4.2c0 1.2 1.8 1.4 2.2 0 .9-3.4-1.6-6.7-5.2-6.7a5.5 5.5 0 1 0 2.8 10.2" fill="none" stroke="#fff" stroke-width="1.8" stroke-linecap="round"/>
        </svg>
        <span>fowler@tamselbriargifts.example</span>
      </li>
      <li class="contact-item">
        <svg class="contact-icon" viewBox="0 0 24 24" aria-hidden="true">
          <circle cx="12" cy="12" r="12" fill="var(--magenta)"/>
          <circle cx="12" cy="12" r="6.5" fill="none" stroke="#fff" stroke-width="1.5"/>
          <ellipse cx="12" cy="12" rx="2.8" ry="6.5" fill="none" stroke="#fff" stroke-width="1.3"/>
          <path d="M5.5 12h13" stroke="#fff" stroke-width="1.3"/>
        </svg>
        <span>www.tamselbriargifts.example</span>
      </li>
    </ul>

    <div class="gold-rule"></div>
    <div class="base-band"></div>
  </main>
</body>
</html>
```